I need a flyer made , the flyer can be one page or two pages or three pages . I will be posting this on Instagram and social media platforms. I am a luxury home builder , I am looking to hire a construction project manager . Below are some examples and ideas what can be on the flyer

We’re looking for a construction project manager who’s passionate about building luxury homes at the highest standards
We’re hiring construction project manager
* Experience 5+ years in residential project management with a strong portfolio of completed homes.
* location : Bergen County NJ
* excellent leadership skills, leads teams with confidence and clarity
* communicates seamlessly with architects , engineers, designers and clients
*knows how to manage budgets and timelines without compromising quality
*solves problems with a positive solution first mindset
* pays attention to every detail because in luxury the small things are the big things

Apply now , link in bio or DM to connect.

My logo is attached, my web site www.pinecrestbuildworks.com
My style is modern but still warm and inviting. I like a clean classy look .
Updates

Please don’t add any images of chairs or people to the flyer , I do not want people on my flyer. Do not add standard images of offices and houses , we are luxury builders , we build homes over 2 million dollars. Keep a classy , simple modern look . High end .

You can add a white hard hat with my logo on it for a image , this is a suggestion does not have to be on my flyer ,

```html
<!DOCTYPE html>
<html lang="en">
<head>
<meta charset="UTF-8">
<title>Hiring – Construction Project Manager</title>
<link href="https://fonts.googleapis.com/css2?family=Playfair+Display:ital,wght@0,400;0,500;1,700&family=Roboto:wght@400;500&family=Roboto+Condensed:wght@700;800&display=swap" rel="stylesheet">
<style>
  :root {
    --ink: #111111;
    --paper: #ffffff;
    --accent: #f6d64a;
    --rule: #c9c9c9;
    --text: #1c1c1c;
    --hat-yellow: #f3d657;
    --gear-green: #cfe3c9;
    --teal: #6cc7b4;
  }
  * { margin: 0; padding: 0; box-sizing: border-box; }
  html, body { width: 927px; height: 1200px; overflow: hidden; background: var(--paper); }
  .flyer { position: relative; width: 927px; height: 1200px; background: var(--paper); overflow: hidden; font-family: "Roboto", Arial, sans-serif; color: var(--text); }

  .speech-bubble { position: absolute; left: 0; top: 0; width: 927px; height: 480px; }

  .headline-small { position: absolute; left: 0; width: 927px; top: 70px; text-align: center; font-family: "Playfair Display", Georgia, serif; font-weight: 400; font-size: 56px; color: var(--paper); line-height: 1; padding-left: 30px; }
  .headline-big { position: absolute; left: 194px; top: 124px; font-family: "Playfair Display", Georgia, serif; font-weight: 400; font-size: 176px; color: var(--paper); line-height: 1; letter-spacing: 0; }
  .headline-bang { position: absolute; left: 780px; top: 62px; font-family: "Playfair Display", Georgia, serif; font-style: italic; font-weight: 700; font-size: 230px; color: var(--accent); line-height: 1; transform: rotate(8deg); }

  .role { position: absolute; left: 38px; width: 457px; top: 472px; text-align: center; font-family: "Playfair Display", Georgia, serif; color: var(--ink); }
  .role-kicker { font-size: 24px; font-weight: 400; letter-spacing: 1px; line-height: 1; }
  .role-title { font-size: 41px; font-weight: 400; letter-spacing: 1px; line-height: 1; margin-top: 10px; }
  .role-rule { position: absolute; left: 38px; top: 561px; width: 457px; height: 5px; background: var(--ink); }

  .requirements { position: absolute; left: 38px; top: 566px; width: 457px; list-style: none; }
  .requirements li { border-bottom: 1.5px solid var(--rule); font-size: 17px; line-height: 23px; display: flex; flex-direction: column; justify-content: center; }
  .requirements li:nth-child(1) { height: 85px; }
  .requirements li:nth-child(2) { height: 61px; }
  .requirements li:nth-child(3) { height: 71px; }
  .requirements li:nth-child(4) { height: 70px; }
  .requirements li:nth-child(5) { height: 71px; }
  .requirements li:nth-child(6) { height: 47px; }
  .requirements li:nth-child(7) { height: 74px; }
  .lead { font-size: 24px; font-weight: 500; }
  .label { font-family: "Roboto Condensed", Arial, sans-serif; font-weight: 800; font-size: 22px; }
  .location { font-size: 22px; }

  .hat-illustration { position: absolute; left: 580px; top: 535px; width: 300px; height: 320px; border-radius: 50% 50% 44% 44%; background: radial-gradient(ellipse at 50% 50%, var(--hat-yellow) 0%, var(--hat-yellow) 32%, var(--gear-green) 58%, var(--teal) 82%, rgba(255,255,255,0) 100%); opacity: 0.9; }

  .brand-name { position: absolute; left: 560px; width: 330px; top: 888px; text-align: center; font-family: "Playfair Display", Georgia, serif; font-size: 36px; line-height: 42px; color: var(--ink); letter-spacing: 1px; }
  .brand-tagline { position: absolute; left: 560px; width: 330px; top: 1010px; text-align: center; font-family: "Playfair Display", Georgia, serif; font-size: 22px; color: var(--ink); letter-spacing: 0.5px; }

  .apply-button { position: absolute; left: 100px; top: 1078px; width: 294px; height: 64px; }
  .apply-button text { font-family: "Roboto Condensed", Arial, sans-serif; font-weight: 800; font-size: 34px; }

  .website { position: absolute; left: 465px; width: 420px; top: 1100px; text-align: center; font-family: "Roboto", Arial, sans-serif; font-size: 18px; letter-spacing: 4px; color: var(--ink); }
</style>
</head>
<body>
<main class="flyer">
  <svg class="speech-bubble" viewBox="0 0 927 480" aria-hidden="true">
    <ellipse cx="440" cy="80" rx="660" ry="340" fill="var(--ink)"/>
    <polygon points="620,380 780,330 690,472" fill="var(--ink)"/>
  </svg>
  <div class="headline-small">We’re</div>
  <h1 class="headline-big">HIRING</h1>
  <div class="headline-bang">!</div>

  <div class="role">
    <div class="role-kicker">CONSTRUCTION</div>
    <h2 class="role-title">PROJECT MANAGER</h2>
  </div>
  <div class="role-rule"></div>

  <ul class="requirements">
    <li><span><span class="lead">Experience 5+</span> years in residential project</span><span>management with a strong portfolio of completed homes.</span></li>
    <li><span><span class="label">LOCATION</span> <span class="location">: Bergen County NJ</span></span></li>
    <li><span>Excellent leadership skills,</span><span>leads teams with confidence and clarity</span></li>
    <li><span>Communicates seamlessly with architects,</span><span>engineers, designers and clients</span></li>
    <li><span>Knows how to manage budgets and timelines</span><span>without compromising quality</span></li>
    <li><span>Solves problems with a positive solution first mindset</span></li>
    <li><span>Pays attention to every detail because in luxury the</span><span>small things are the big things</span></li>
  </ul>

  <div class="hat-illustration" role="img" aria-label="Illustration of a yellow hard hat surrounded by gears, rulers, a crane and construction tools"></div>

  <div class="brand-name">PINECREST<br>BUILDWORKS</div>
  <div class="brand-tagline">CRAFTED. REFINED. HOME.</div>

  <svg class="apply-button" viewBox="0 0 294 64" role="img" aria-label="Apply now">
    <path d="M14 0 H170 V64 H14 L0 50 V14 Z" fill="var(--ink)"/>
    <path d="M160 0 H278 L294 32 L278 64 H160 Z" fill="var(--accent)"/>
    <text x="22" y="45" fill="var(--paper)">APPLY</text>
    <text x="168" y="45" fill="var(--ink)">NOW!</text>
  </svg>

  <div class="website">WWW.PINECRESTBUILDWORKS.COM</div>
</main>
</body>
</html>
```